Design an Elegant Handbag Brand website

I need a webiste design are looking for ideas for a new theme, color scheme, etc. You come up with the general look and feel of the home page and our team will take it from there.
We're only looking for a one (1) page layout which should be fashionable and graphic intensive, but also include the standard homepage links (about us, see our collections, etc)

Target Market(s)

Our customers are fashionable women looking for an animal friendly and environmentally friendly handbag.

Industry/Entity Type

Business

Number of Pages Required

1 page

Font styles to use
Serif
Sans Serif

Requirements
Must have
• Feel free to modify it with different colors or tweaks as you see fit. We are open to all suggestions.
Nice to have

```html
<!DOCTYPE html>
<html lang="en">
<head>
<meta charset="utf-8">
<title>Velina — Handbags</title>
<link href="https://fonts.googleapis.com/css2?family=Montserrat:wght@300;400;500;600&family=Playfair+Display:wght@900&family=Roboto:wght@300;400&display=swap" rel="stylesheet">
<style>
:root{
  --ink:#2b2b2d;
  --muted:#8f8f8f;
  --hero-bg:#f9f0cf;
  --arrivals-bg:#f6f2f3;
  --footer-bg:#f7f6f6;
  --accent:#e8a796;
  --card-bg:#f5f5f5;
  --overlay:#c5bdbb;
  --sale-price:#3e2c22;
  --taupe:rgba(176,148,118,.9);
  --taupe-soft:rgba(176,148,118,0);
}
*{margin:0;padding:0;box-sizing:border-box}
html,body{width:1200px;height:2774px;overflow:hidden}
body{position:relative;background:#fff;font-family:'Montserrat',sans-serif;color:var(--ink)}
.abs{position:absolute}
.brand{font-family:'Montserrat',sans-serif;font-weight:500;font-size:15px;letter-spacing:3px;color:var(--ink)}
.site-header .brand{left:62px;top:27px}
.main-nav{left:434px;top:31px;display:flex;gap:42px;font-size:10px;letter-spacing:1.6px}
.main-nav a{color:var(--ink);text-decoration:none}
.main-nav a.active{text-decoration:underline;text-underline-offset:4px}
.header-icons{left:1042px;top:26px;display:flex;gap:22px}
.side-social{left:26px;top:160px;width:14px;height:340px}
.side-social span{position:absolute;left:0;transform:rotate(-90deg);transform-origin:left top;font-size:9px;letter-spacing:1.5px;color:#a9a9a9;white-space:nowrap}
.slider-dots{left:1147px;top:298px;display:flex;flex-direction:column;align-items:center;gap:6px}
.slider-dots i{display:block;width:5px;height:5px;border-radius:50%;background:#d6d6d6}
.slider-dots i.on{width:9px;height:9px;background:none;border:1px solid #9a9a9a}

.hero{left:56px;top:71px;width:1068px;height:486px;background:var(--hero-bg)}
.hero-copy{left:160px;top:262px;width:270px;text-align:center}
.hero-kicker{font-size:11px;letter-spacing:6px;font-weight:500;display:flex;align-items:center;justify-content:center;gap:14px}
.hero-kicker::before,.hero-kicker::after{content:"";width:22px;height:2px;background:var(--accent)}
.hero-title{font-family:'Playfair Display',serif;font-weight:900;font-size:44px;letter-spacing:7px;margin-top:2px;line-height:1.1}
.hero-rule{width:22px;height:2px;background:var(--accent);margin:10px auto 0}
.hero-sub{font-size:11px;letter-spacing:2px;font-weight:500;margin-top:14px}
.btn{display:inline-block;background:var(--ink);color:#fff;font-size:10px;letter-spacing:2px;font-weight:500;text-align:center;text-decoration:none}
.hero-copy .btn{margin-top:36px;width:111px;height:27px;line-height:27px}
.hero-ring{left:526px;top:140px;width:348px;height:348px;border-radius:50%;border:5px solid #fbf5e2}
.hero-bag{left:600px;top:165px;width:340px;height:300px;background:radial-gradient(ellipse 50% 48% at 50% 55%,var(--taupe) 0%,rgba(176,148,118,.55) 55%,var(--taupe-soft) 100%)}

.arrivals{left:56px;top:582px;width:1068px;height:486px;background:var(--arrivals-bg)}
.arrivals-photo{left:100px;top:582px;width:380px;height:486px;background:radial-gradient(ellipse 48% 60% at 50% 62%,rgba(178,132,96,.85) 0%,rgba(196,160,130,.5) 55%,rgba(246,242,243,0) 100%)}
.arrivals-bag{left:520px;top:715px;width:170px;height:220px;background:radial-gradient(ellipse 48% 44% at 50% 60%,rgba(28,28,30,.95) 0%,rgba(28,28,30,.7) 60%,rgba(28,28,30,0) 100%)}
.arrivals-copy{left:736px;top:777px;width:310px}
.eyebrow{font-size:10px;letter-spacing:2.4px;font-weight:500}
.arrivals-copy p{font-size:9px;letter-spacing:2px;line-height:12px;color:#7a6a64;margin-top:28px}
.arrivals-copy .btn{margin-top:30px;width:111px;height:26px;line-height:26px}

.section-title{left:56px;font-size:10px;letter-spacing:2.4px;font-weight:500}
.card{width:178px;height:224px;background:var(--card-bg);border:1px solid #f0f0f0;overflow:hidden}
.card.white{background:#fff}
.card .heart{position:absolute;right:14px;top:14px}
.card .product{position:absolute;left:4px;right:4px;top:20px;height:190px;background:radial-gradient(ellipse 46% 40% at 50% 60%,var(--tone) 0%,var(--tone-mid) 60%,transparent 100%)}
.card .add{position:absolute;left:0;right:0;bottom:0;height:40px;line-height:40px;background:var(--overlay);color:#fff;font-size:10px;letter-spacing:2.4px;text-align:center}
.bag-pink{--tone:rgba(232,168,152,.9);--tone-mid:rgba(232,168,152,.45)}
.bag-gold{--tone:rgba(206,182,120,.9);--tone-mid:rgba(206,182,120,.45)}
.bag-cream{--tone:rgba(228,216,196,.95);--tone-mid:rgba(228,216,196,.5)}
.bag-blush{--tone:rgba(238,190,178,.9);--tone-mid:rgba(238,190,178,.45)}
.bag-black{--tone:rgba(30,30,32,.92);--tone-mid:rgba(30,30,32,.45)}
.card-meta{width:178px;text-align:center}
.card-meta .name{font-size:10px;letter-spacing:2px;color:var(--muted)}
.card-meta .price{font-size:10px;letter-spacing:2px;font-weight:500;margin-top:12px}

.sale{left:56px;top:1910px;width:1068px;height:486px;background:linear-gradient(180deg,#f7ebe3,#fbf3ee)}
.sale-bag{left:420px;top:2010px;width:360px;height:300px;background:radial-gradient(ellipse 48% 46% at 50% 55%,var(--taupe) 0%,rgba(176,148,118,.55) 55%,var(--taupe-soft) 100%)}
.sale-word{left:205px;top:2016px;width:785px;display:flex;justify-content:space-between;font-family:'Roboto',sans-serif;font-weight:300;font-size:262px;line-height:1;color:#fff}
.old-price{left:242px;top:2282px;font-family:'Roboto',sans-serif;font-weight:300;font-size:60px;letter-spacing:9px;color:#b1a7a5;text-decoration:line-through;text-decoration-thickness:3px}
.sale-btn{left:523px;top:2313px;width:110px;height:25px;line-height:25px}
.new-price{left:765px;top:2278px;font-family:'Roboto',sans-serif;font-weight:300;font-size:64px;letter-spacing:9px;color:var(--sale-price)}

.site-footer{left:0;top:2475px;width:1200px;height:299px;background:var(--footer-bg)}
.site-footer .brand{left:76px;top:71px}
.footer-about{left:74px;top:112px;width:210px;font-family:'Roboto',sans-serif;font-size:11px;line-height:13px;color:#444}
.footer-about p{text-indent:22px;margin-bottom:13px}
.newsletter-title{left:527px;top:72px;font-size:10px;letter-spacing:2.4px;font-weight:500}
.newsletter-input{left:492px;top:113px;width:171px;height:23px;border-radius:12px;background:#fff;font-size:9px;color:#c5c5c5;padding:6px 0 0 42px}
.newsletter-btn{left:517px;top:160px;width:110px;height:25px;line-height:25px}
.contact{left:891px;top:92px;font-family:'Roboto',sans-serif;font-size:15px;color:#444}
.contact dl{display:grid;grid-template-columns:59px auto;row-gap:22px}
.contact dt{font-size:12px;padding-top:3px}
.footer-social{left:925px;top:218px;display:flex;gap:20px}
.footer-social i{display:block;width:11px;height:11px;border-radius:2px;background:#666}
.copyright{left:0;top:2744px;width:1200px;text-align:center;font-family:'Roboto',sans-serif;font-size:15px;color:#555}
</style>
</head>
<body>

<header class="site-header">
  <div class="abs brand">Velina</div>
  <nav class="abs main-nav">
    <a href="#" class="active">Home</a><a href="#">About us</a><a href="#">Our collection</a><a href="#">Contacts</a>
  </nav>
  <div class="abs header-icons">
    <svg width="18" height="18" viewBox="0 0 18 18" aria-label="Search"><circle cx="7.5" cy="7.5" r="5.5" fill="none" stroke="#2b2b2d" stroke-width="2"/><line x1="11.5" y1="11.5" x2="16" y2="16" stroke="#2b2b2d" stroke-width="2.2" stroke-linecap="round"/></svg>
    <svg width="22" height="20" viewBox="0 0 22 20" aria-label="Cart"><path d="M1 3h3l2.2 9h9.5L18 5H5.2" fill="none" stroke="#2b2b2d" stroke-width="1.6" stroke-linejoin="round"/><circle cx="8" cy="16" r="1.4" fill="#2b2b2d"/><circle cx="14.5" cy="16" r="1.4" fill="#2b2b2d"/><circle cx="18" cy="3" r="3" fill="#2b2b2d"/><text x="18" y="4.6" font-size="4.5" fill="#fff" text-anchor="middle" font-family="Montserrat,sans-serif">2</text></svg>
  </div>
</header>

<div class="abs side-social">
  <span style="top:70px">Boards</span>
  <span style="top:150px">Notes</span>
  <span style="top:240px">Circle</span>
  <span style="top:338px">Gallery</span>
</div>
<div class="abs slider-dots"><i class="on"></i><i></i><i></i></div>

<section class="abs hero"></section>
<div class="abs hero-ring"></div>
<div class="abs hero-bag" role="img" aria-label="Set of three taupe leather handbags with tassel and chain details"></div>
<div class="abs hero-copy">
  <div class="hero-kicker">STYLE</div>
  <h1 class="hero-title">NATURE</h1>
  <div class="hero-rule"></div>
  <div class="hero-sub">NEW COLLECTION</div>
  <a class="btn">See collection</a>
</div>

<section class="abs arrivals"></section>
<div class="abs arrivals-photo" role="img" aria-label="Two women in camel coats posing with a beige clutch"></div>
<div class="abs arrivals-bag" role="img" aria-label="Black leather tote bag"></div>
<div class="abs arrivals-copy">
  <div class="eyebrow">NEW ARRIVALS</div>
  <p>Lorem ipsum dolor sit amet, consectetuer ad-ipiscing elit, sed diam nonummy nibh euismod tincidunt ut laoreet dolore magna aliquam erat volutpat. Ut wisi enim ad minim</p>
  <a class="btn">See collection</a>
</div>

<h2 class="abs section-title" style="top:1138px">BESTSELLLERS</h2>

<div class="abs card white" style="left:83px;top:1190px"><div class="product bag-pink" role="img" aria-label="Pink handbag set"></div><svg class="heart" width="22" height="20" viewBox="0 0 22 20"><path d="M11 18S2 12 2 6.5A4.5 4.5 0 0 1 11 4a4.5 4.5 0 0 1 9 2.5C20 12 11 18 11 18z" fill="none" stroke="#b0b0b0" stroke-width="1.3"/></svg></div>
<div class="abs card" style="left:292px;top:1190px"><div class="product bag-gold" role="img" aria-label="Gold handbag set"></div><svg class="heart" width="22" height="20" viewBox="0 0 22 20"><path d="M11 18S2 12 2 6.5A4.5 4.5 0 0 1 11 4a4.5 4.5 0 0 1 9 2.5C20 12 11 18 11 18z" fill="none" stroke="#b0b0b0" stroke-width="1.3"/></svg></div>
<div class="abs card white" style="left:501px;top:1190px"><div class="product bag-cream" role="img" aria-label="Cream handbag set"></div><svg class="heart" width="22" height="20" viewBox="0 0 22 20"><path d="M11 18S2 12 2 6.5A4.5 4.5 0 0 1 11 4a4.5 4.5 0 0 1 9 2.5C20 12 11 18 11 18z" fill="none" stroke="#b0b0b0" stroke-width="1.3"/></svg><div class="add">ADD TO CART</div></div>
<div class="abs card white" style="left:710px;top:1190px"><div class="product bag-blush" role="img" aria-label="Blush dome handbag"></div><svg class="heart" width="22" height="20" viewBox="0 0 22 20"><path d="M11 18S2 12 2 6.5A4.5 4.5 0 0 1 11 4a4.5 4.5 0 0 1 9 2.5C20 12 11 18 11 18z" fill="none" stroke="#b0b0b0" stroke-width="1.3"/></svg></div>
<div class="abs card" style="left:918px;top:1190px"><div class="product bag-black" role="img" aria-label="Black quilted handbag"></div><svg class="heart" width="22" height="20" viewBox="0 0 22 20"><path d="M11 18S2 12 2 6.5A4.5 4.5 0 0 1 11 4a4.5 4.5 0 0 1 9 2.5C20 12 11 18 11 18z" fill="none" stroke="#b0b0b0" stroke-width="1.3"/></svg></div>

<div class="abs card-meta" style="left:80px;top:1439px"><div class="name">New womens fashion</div><div class="price">299$</div></div>
<div class="abs card-meta" style="left:292px;top:1439px"><div class="name">New womens fashion</div><div class="price">299$</div></div>
<div class="abs card-meta" style="left:504px;top:1439px"><div class="name">New womens fashion</div><div class="price">299$</div></div>
<div class="abs card-meta" style="left:716px;top:1439px"><div class="name">New womens fashion</div><div class="price">299$</div></div>
<div class="abs card-meta" style="left:918px;top:1439px"><div class="name">New womens fashion</div><div class="price">299$</div></div>

<h2 class="abs section-title" style="top:1512px">NEW ARRIVALS</h2>

<div class="abs card white" style="left:83px;top:1541px"><div class="product bag-pink" role="img" aria-label="Pink handbag set"></div><svg class="heart" width="22" height="20" viewBox="0 0 22 20"><path d="M11 18S2 12 2 6.5A4.5 4.5 0 0 1 11 4a4.5 4.5 0 0 1 9 2.5C20 12 11 18 11 18z" fill="none" stroke="#b0b0b0" stroke-width="1.3"/></svg></div>
<div class="abs card" style="left:292px;top:1541px"><div class="product bag-gold" role="img" aria-label="Gold handbag set"></div><svg class="heart" width="22" height="20" viewBox="0 0 22 20"><path d="M11 18S2 12 2 6.5A4.5 4.5 0 0 1 11 4a4.5 4.5 0 0 1 9 2.5C20 12 11 18 11 18z" fill="none" stroke="#b0b0b0" stroke-width="1.3"/></svg></div>
<div class="abs card white" style="left:501px;top:1541px"><div class="product bag-cream" role="img" aria-label="Cream handbag set"></div><svg class="heart" width="22" height="20" viewBox="0 0 22 20"><path d="M11 18S2 12 2 6.5A4.5 4.5 0 0 1 11 4a4.5 4.5 0 0 1 9 2.5C20 12 11 18 11 18z" fill="none" stroke="#b0b0b0" stroke-width="1.3"/></svg></div>
<div class="abs card white" style="left:710px;top:1541px"><div class="product bag-blush" role="img" aria-label="Blush dome handbag"></div><svg class="heart" width="22" height="20" viewBox="0 0 22 20"><path d="M11 18S2 12 2 6.5A4.5 4.5 0 0 1 11 4a4.5 4.5 0 0 1 9 2.5C20 12 11 18 11 18z" fill="none" stroke="#b0b0b0" stroke-width="1.3"/></svg></div>
<div class="abs card" style="left:918px;top:1541px"><div class="product bag-black" role="img" aria-label="Black quilted handbag"></div><svg class="heart" width="22" height="20" viewBox="0 0 22 20"><path d="M11 18S2 12 2 6.5A4.5 4.5 0 0 1 11 4a4.5 4.5 0 0 1 9 2.5C20 12 11 18 11 18z" fill="none" stroke="#b0b0b0" stroke-width="1.3"/></svg></div>

<div class="abs card-meta" style="left:80px;top:1790px"><div class="name">New womens fashion</div><div class="price">299$</div></div>
<div class="abs card-meta" style="left:292px;top:1790px"><div class="name">New womens fashion</div><div class="price">299$</div></div>
<div class="abs card-meta" style="left:504px;top:1790px"><div class="name">New womens fashion</div><div class="price">299$</div></div>
<div class="abs card-meta" style="left:716px;top:1790px"><div class="name">New womens fashion</div><div class="price">299$</div></div>
<div class="abs card-meta" style="left:918px;top:1790px"><div class="name">New womens fashion</div><div class="price">299$</div></div>

<section class="abs sale"></section>
<div class="abs sale-bag" role="img" aria-label="Set of taupe leather handbags on sale"></div>
<div class="abs sale-word"><span>S</span><span>A</span><span>L</span><span>E</span></div>
<div class="abs old-price">499$</div>
<a class="abs btn sale-btn">ADD TO CART</a>
<div class="abs new-price">299$</div>

<footer class="abs site-footer">
  <div class="abs brand">Velina</div>
  <div class="abs footer-about">
    <p>Lorem ipsum dolor sit amet, consec-tetuer adipiscing elit, sed diam nonummy nibh euismod tincidunt ut laoreet dolore magna aliquam erat</p>
    <p>Lorem ipsum dolor sit amet, consec-tetuer adipiscing elit</p>
  </div>
  <div class="abs newsletter-title">NEWSLETTER</div>
  <div class="abs newsletter-input">Email</div>
  <a class="abs btn newsletter-btn">Join news</a>
  <div class="abs contact">
    <dl>
      <dt>Cell :</dt><dd>+1 555 014 2290</dd>
      <dt>Email :</dt><dd>hello@velina.example<br>care@velina.example</dd>
    </dl>
  </div>
  <div class="abs footer-social"><i></i><i></i><i></i><i></i></div>
</footer>
<div class="abs copyright">© 2020 &nbsp; All rights reserved</div>

</body>
</html>
```